"Orchard Bell Eats" labels for food items

We're a vending service company that serves fresh food to some of our customers. We'd like an attractive label to place on our food options that identifies our brand.

We have a current label design for the coffee we provide to our clients. We would like our food label design to be complimentary to that design. That label has been included with this project.

The basic concept of the design we're looking for is an identifiable peach, the state fruit, wearing a chef's hat with a simple smiling "chef's" face. There are some concept ideas included with this project as well.

These labels will be placed on food item containers such as sandwiches, salads, etc.

Logo Text

Orchard Bell Eats

Colors

Designer to choose colors to be used in the design.

Requirements
Must have
• Identifiable peach, chef's hat
Nice to have
• compliment current coffee design

```html
<!DOCTYPE html>
<html lang="en">
<head>
<meta charset="utf-8">
<title>Orchard Bell Eats – Chicken Salad Label</title>
<link rel="stylesheet" href="https://fonts.googleapis.com/css2?family=Cinzel:wght@500;600&family=Montserrat:wght@500&display=swap">
<style>
  :root {
    --backdrop: #1c1c1e;
    --label-white: #ffffff;
    --peach-deep: #ff5a0f;
    --peach-soft: #f3977a;
    --ink: #111111;
    --band-grey: #efefef;
    --stitch: #555555;
    --caption-grey: #6a6a6a;
  }
  html, body {
    margin: 0;
    width: 1200px;
    height: 1081px;
    overflow: hidden;
    background: var(--backdrop);
  }
  .label {
    position: absolute;
    left: 100px;
    top: 40px;
    width: 1000px;
    height: 1000px;
  }
  .label-face { fill: var(--label-white); }
  .stitch-line {
    fill: none;
    stroke: var(--stitch);
    stroke-width: 1.6;
    stroke-dasharray: 7 5;
  }
  .title-band { fill: var(--band-grey); }
  .brand-mark { fill: var(--peach-deep); }
  .brand-name {
    font-family: "Cinzel", serif;
    font-weight: 600;
    font-size: 62px;
    fill: var(--ink);
  }
  .product-name {
    font-family: "Cinzel", serif;
    font-weight: 500;
    font-size: 62px;
    fill: var(--ink);
  }
  .product-note {
    font-family: "Montserrat", sans-serif;
    font-weight: 500;
    font-size: 20px;
    letter-spacing: 5px;
    fill: var(--caption-grey);
  }
</style>
</head>
<body>
<svg class="label" viewBox="-500 -500 1000 1000" xmlns="http://www.w3.org/2000/svg">
  <defs>
    <clipPath id="label-shape">
      <polygon points="0,-450 370,-368 452,0 360,372 0,450 -355,365 -452,0 -368,-365"/>
    </clipPath>
    <linearGradient id="swoosh-top" x1="0" y1="0" x2="1" y2="0.3">
      <stop offset="0" stop-color="#ffffff"/>
      <stop offset="0.45" stop-color="var(--peach-soft)"/>
      <stop offset="1" stop-color="var(--peach-deep)"/>
    </linearGradient>
    <linearGradient id="swoosh-bottom" x1="0" y1="0" x2="1" y2="0.4">
      <stop offset="0" stop-color="var(--peach-deep)"/>
      <stop offset="0.6" stop-color="var(--peach-soft)"/>
      <stop offset="1" stop-color="#ffffff"/>
    </linearGradient>
  </defs>

  <polygon class="label-face" points="0,-450 370,-368 452,0 360,372 0,450 -355,365 -452,0 -368,-365"/>

  <g clip-path="url(#label-shape)">
    <path fill="url(#swoosh-top)" d="M60,-430 C200,-400 330,-330 420,-200 L480,-200 L480,-480 L60,-480 Z"/>
    <path fill="url(#swoosh-bottom)" d="M-470,0 C-380,20 -320,130 -280,260 C-250,350 -180,400 -60,430 L-60,480 L-480,480 Z"/>
  </g>

  <polygon class="stitch-line" points="0,-430 352,-352 432,0 343,355 0,430 -338,348 -432,0 -350,-348"/>

  <circle class="brand-mark" cx="0" cy="-120" r="150"/>
  <text class="brand-name" x="0" y="140" text-anchor="middle">Orchard Bell Eats</text>

  <rect class="title-band" x="-270" y="256" width="610" height="74"/>
  <text class="product-name" x="0" y="314" text-anchor="middle">Chicken Salad</text>
  <text class="product-note" x="0" y="358" text-anchor="middle">- MADE WITH WHITE MEAT -</text>
</svg>
</body>
</html>
```